Webdesign für psychotherapeutische Praxis
Zielgruppe
Psychotherapeutische Praxis für erwachsene Patienten mit psychischen Erkrankungen.
Die Website soll eine solide, vertrauensvolle Information über das therapeutische Angebot bieten sowie alle Informationen zur Erstkontaktaufnahme erhalten.
Aufgabenstellung
Logo füge ich bei. Die Farben, das Design, die Schrift sollen dem Logo entsprechen (Grau, Violett-Pink Töne, moderne Schrift).

```html
<!DOCTYPE html>
<html lang="de">
<head>
<meta charset="utf-8">
<title>Psychotherapeutische Praxis – Miriam Hollmann</title>
<link href="https://fonts.googleapis.com/css2?family=Fira+Sans:wght@300;400;500;700&display=swap" rel="stylesheet">
<style>
:root{
  --violet:#6a56a4;
  --pink:#c1599f;
  --text:#555;
  --heading:#444;
  --light:#f1f0f8;
  --white:#fff;
}
*{box-sizing:border-box;margin:0;padding:0}
html,body{width:718px;height:1200px;overflow:hidden}
body{position:relative;font-family:"Fira Sans",sans-serif;font-weight:300;color:var(--text);background:var(--white)}
.abs{position:absolute}
.topbar{left:0;top:0;width:718px;height:17px;background:linear-gradient(90deg,var(--violet),var(--pink) 50%,var(--violet))}
.topbar .contact{position:absolute;top:0;height:17px;display:flex;align-items:center;gap:3px;color:#fff;font-size:5px;font-weight:400;padding:0 9px;border-left:1px solid rgba(255,255,255,.3)}
.menu-icon{position:absolute;left:579px;top:6px;width:8px}
.menu-icon span{display:block;height:1px;background:#fff;margin-bottom:1.5px}
.brand{left:131px;top:0;width:192px;height:43px;background:#fff;box-shadow:0 2px 6px rgba(0,0,0,.12);display:flex;align-items:center;gap:30px;padding-left:18px}
.brand .dot{width:18px;height:18px;border-radius:50%;background:var(--violet);flex:none}
.brand .name{color:var(--heading);font-weight:400;font-size:7.8px;line-height:1.35;letter-spacing:.2px}
.brand .name small{display:block;font-size:4.3px;font-weight:300}
.nav{top:17px;left:0;width:718px;height:24px;background:#fff}
.nav ul{list-style:none;position:absolute;right:136px;top:8px;display:flex;gap:9px;font-size:6.3px;font-weight:300;color:var(--heading)}
.nav li.active{color:var(--pink)}
.hero{left:0;top:41px;width:718px;height:254px;background:linear-gradient(160deg,#8fb3d9 0%,#e9d88b 30%,#f2c23a 60%,#d59a18 100%)}
.hero-frame{left:138px;top:41px;width:442px;height:172px;border:6px solid rgba(255,255,255,.45)}
.hero-frame::after{content:"";position:absolute;inset:1px;border:2px solid rgba(255,255,255,.85)}
.hero h1{position:absolute;left:0;right:0;top:109px;text-align:center;color:#fff;font-weight:700;font-size:33px;letter-spacing:-.5px}
.hero p{position:absolute;right:195px;top:145px;width:200px;text-align:right;font-size:6.8px;color:#6b5420;line-height:1.22}
.praxis{left:0;top:295px;width:718px;height:278px;background:linear-gradient(180deg,#f3f2f2,#ecebec);clip-path:polygon(0 0,100% 0,100% 254px,0 277px)}
.sec-title{display:flex;align-items:center;gap:8px;font-weight:300;color:var(--heading)}
.sec-title::before{content:"";width:15px;height:1.5px;background:var(--violet)}
.praxis .sec-title{position:absolute;left:134px;top:44px;font-size:13.5px}
.praxis .copy{position:absolute;left:134px;top:69px;width:210px;font-size:6px;line-height:1.35}
.copy p{margin-bottom:7px}
.copy b{font-weight:500;color:var(--heading)}
.btn{position:absolute;height:19px;border-radius:10px;background:var(--pink);color:#fff;font-size:5.8px;font-weight:400;letter-spacing:.3px;display:flex;align-items:center;justify-content:center;gap:6px}
.hours-title{position:absolute;left:134px;top:179px;display:flex;align-items:center;gap:3px;color:var(--violet);font-size:7.3px;font-weight:400}
.hours{position:absolute;top:195px;font-size:6px;line-height:1.33;display:grid;grid-template-columns:42px auto}
.photo{position:absolute}
.andrea .sec-title{position:absolute;left:131px;top:82px;font-size:13.5px}
.andrea{left:0;top:573px;width:718px;height:267px}
.andrea .copy{position:absolute;left:131px;top:104px;width:148px;font-size:6px;line-height:1.35}
.card{position:absolute;width:132px;background:#fff;box-shadow:0 2px 10px rgba(0,0,0,.09);padding:15px 15px 0}
.card .icon{width:20px;height:26px;border-radius:5px;background:linear-gradient(135deg,var(--violet),var(--pink));opacity:.75}
.card h3{margin-top:18px;font-size:7.8px;font-weight:400;color:var(--violet)}
.card p{margin-top:8px;font-size:5.8px;line-height:1.35}
.card a{display:inline-block;margin-top:7px;font-size:5.5px;font-weight:500;color:var(--pink);text-decoration:underline}
.kontakt{left:0;top:840px;width:718px;height:198px;background:linear-gradient(180deg,#f6f2ef,#eceae9 60%,#e4e3e5)}
.kontakt h2{position:absolute;left:0;right:0;top:40px;text-align:center;font-size:14px;font-weight:300;color:var(--heading)}
.kontakt .rule{position:absolute;left:350px;top:58px;width:18px;height:1.5px;background:var(--violet)}
.kontakt p{position:absolute;left:0;right:0;top:89px;text-align:center;font-size:7.5px;line-height:1.25}
.footer{left:0;top:1038px;width:718px;height:118px;background:var(--light)}
.footer .accent{position:absolute;left:131px;top:-2px;width:299px;height:2px;background:var(--pink)}
.footer .brand-f{position:absolute;left:145px;top:25px;display:flex;align-items:center;gap:20px}
.footer .brand-f .dot{width:14px;height:14px;border-radius:50%;background:var(--violet)}
.footer .brand-f .name{font-size:5px;font-weight:400;color:var(--heading);line-height:1.3}
.footer .brand-f small{display:block;font-size:3px}
.footer .about{position:absolute;left:145px;top:55px;width:270px;font-size:5px;line-height:1.6}
.links{position:absolute;top:24px;width:63px;list-style:none;font-size:5.2px;font-weight:400}
.links li{border-bottom:1px solid #cfcde0;padding:1px 0 3px;margin-bottom:4px;line-height:1.5}
.links li:last-child{border:none}
.bottombar{left:0;top:1156px;width:718px;height:44px;background:linear-gradient(180deg,var(--violet),#a55ea8 60%,var(--pink))}
.bottombar p{position:absolute;left:131px;top:20px;color:#fff;font-size:5.3px;font-weight:500}
.up{position:absolute;left:570px;top:15px;width:17px;height:17px;border:1px solid #fff;display:flex;align-items:center;justify-content:center}
</style>
</head>
<body>

<div class="abs topbar">
  <div class="contact" style="left:324px;width:58px;border-left:none">
    <svg width="5" height="5" viewBox="0 0 10 10"><path d="M2 1l2 2-1 1.5c.7 1.4 1.6 2.3 3 3L7.5 6l2 2-1.5 1.5C4.5 9 1 5.5.5 2.5z" fill="#fff"/></svg>0123 987 6540</div>
  <div class="contact" style="left:382px;width:94px;border-right:1px solid rgba(255,255,255,.3)">
    <svg width="5" height="4" viewBox="0 0 10 8"><rect x=".5" y=".5" width="9" height="7" fill="none" stroke="#fff"/><path d="M.5.5L5 4.5 9.5.5" fill="none" stroke="#fff"/></svg>info@hollmann-therapie.de</div>
  <div class="menu-icon"><span></span><span></span><span></span></div>
</div>

<div class="abs nav">
  <ul><li class="active">Startseite</li><li>Therapieangebot</li><li>Therapieablauf</li><li>Über mich</li><li>Kontakt</li></ul>
</div>

<div class="abs brand">
  <div class="dot"></div>
  <div class="name">Psychotherapeutische Praxis<br>DIPL.-PSYCH. MIRIAM HOLLMANN<small>Psychologische Psychotherapeutin (VT)</small></div>
</div>

<section class="abs hero" role="img" aria-label="Foto: Frau mit ausgebreiteten Armen in einem sonnigen Kornfeld">
  <div class="abs hero-frame"></div>
  <h1>Herzlich Willkommen</h1>
  <p>Muster Willkommenstext Lorem ipsum dolor sit amet consetetur sadipscing elitr, sed diam nonumy eirmod tempor invidunt ilabore et dolore magna aliquyam erat, sed diam voluptua!</p>
</section>

<section class="abs praxis">
  <h2 class="sec-title">Praxis</h2>
  <div class="copy">
    <p>Herzlich Willkommen bei <b>Psychotherapeutische Praxis – Miriam Hollmann</b></p>
    <p>Wir sind gern für Sie da und sehr bemüht, Ihnen zeitnah einen Therapieplatz anzubieten.<br>Hier finden Sie Informationen über unsere Praxis, Therapieangebot und Therapieablauf. Wir möchten Sie einladen, sich hier einen ersten Eindruck über unser Therapieangebot zu verschaffen oder gern direkt mit uns Kontakt aufzunehmen.</p>
  </div>
  <div class="btn" style="left:134px;top:145px;width:119px">JETZT KONTAKT AUFNEHMEN
    <svg width="10" height="4" viewBox="0 0 20 8"><path d="M0 4h18M14 1l4 3-4 3" fill="none" stroke="#fff"/></svg></div>
  <div class="hours-title">
    <svg width="8" height="8" viewBox="0 0 10 10"><circle cx="5" cy="5" r="4.3" fill="none" stroke="var(--violet)"/><path d="M5 2.5V5l1.8 1.2" fill="none" stroke="var(--violet)"/></svg>Öffnungszeiten:</div>
  <div class="hours" style="left:134px"><span>Montag:</span><span>09:00–20:00</span><span>Dienstag:</span><span>09:00–20:00</span><span>Mittwoch:</span><span>09:00–20:00</span><span>Donnerstag:</span><span>09:00–20:00</span></div>
  <div class="hours" style="left:243px;grid-template-columns:37px auto"><span>Freitag:</span><span>09:00–20:00</span><span>Samstag:</span><span>10:00–14:00</span><span>Sonntag:</span><span>&nbsp;Geschlossen</span></div>
  <div class="photo" style="left:489px;top:51px;width:101px;height:106px;background:linear-gradient(160deg,#9a9a98,#d9d8d4 50%,#4a4a48)" role="img" aria-label="Foto: Eingang des Praxisgebäudes mit Torbogen"></div>
  <div class="photo" style="left:359px;top:92px;width:151px;height:99px;background:linear-gradient(135deg,#eeeeee,#d8d5cf 60%,#b59a74)" role="img" aria-label="Foto: heller Empfangsbereich der Praxis"></div>
</section>

<section class="abs andrea">
  <h2 class="sec-title">Miriam Hollmann</h2>
  <div class="copy">
    <p>Muster Text dolor sit amet, consetetur sadipscing elitr, sed diam nonumy eirmod tempor invidunt ut labore et dolore magna aliquyam erat, sed diam voluptua estil vero eos et <b>accusam et justo duo dolores</b> et ea rebum. Stet clita kasd gubergren no sea takimata sanctus est Lorem ipsum dolor sit amet. Lorem ipsum dolor sit amet, consetetur sadipscing elitr.</p>
    <p>Sed diam nonumy eirmod tempor invidunt ut labore et dolore et magna aliquyam erat, sed diam voluptua. At vero eos et accusam.</p>
  </div>
  <div class="btn" style="left:131px;top:205px;width:65px">ÜBER MICH
    <svg width="10" height="4" viewBox="0 0 20 8"><path d="M0 4h18M14 1l4 3-4 3" fill="none" stroke="#fff"/></svg></div>
  <div class="card" style="left:293px;top:55px;height:134px">
    <div class="icon" role="img" aria-label="Symbol: Kopf mit Baum"></div>
    <h3>Therapieangebot</h3>
    <p>Lorem ipsum dolor sit amet, consectetur adipiscing elit. Ut elit tellus, luctus nec ullamcorper mattis, pulvinar dapibus leo.</p>
    <a>MEHR ERFAHREN</a>
  </div>
  <div class="card" style="left:448px;top:33px;height:134px">
    <div class="icon" role="img" aria-label="Symbol: Kreise mit Pfeilen"></div>
    <h3>Therapieablauf</h3>
    <p>Lorem ipsum dolor sit amet, consectetur adipiscing elit. Ut elit tellus, luctus nec ullamcorper mattis, pulvinar dapibus leo.</p>
    <a>MEHR ERFAHREN</a>
  </div>
</section>

<section class="abs kontakt" role="img" aria-label="Unscharfes Stadtbild im Hintergrund">
  <h2>Kontakt</h2>
  <div class="rule"></div>
  <p>Bei Fragen stehen wir Ihnen gerne zur Verfügung. Am besten erreichen Sie uns<br>via E-Mail oder über das Kontaktformular.</p>
  <div class="btn" style="left:309px;top:131px;width:100px">KONTAKT AUFNEHMEN
    <svg width="10" height="4" viewBox="0 0 20 8"><path d="M0 4h18M14 1l4 3-4 3" fill="none" stroke="#fff"/></svg></div>
</section>

<footer class="abs footer">
  <div class="accent"></div>
  <div class="brand-f"><div class="dot"></div><div class="name">Psychotherapeutische Praxis<br>DIPL.-PSYCH. MIRIAM HOLLMANN<small>Psychologische Psychotherapeutin (VT)</small></div></div>
  <p class="about">Muster kurze über Praxis Text Etiam magna arcu, ullamcorper ut pulvinar et, ornare sit amet ligula. Aliquam vitae bibendum lorem. Cras id dui lectus. Pellentesque nec felis tristique urna lacinia sollicitudin ac ac ex. Maecenas mattis faucibus condimentum.</p>
  <ul class="links" style="left:445px"><li>Startseite</li><li>Therapieangebot</li><li>Therapieablauf</li><li>Über mich</li><li>Kontakt</li></ul>
  <ul class="links" style="left:523px"><li>Impressum</li><li>Datenschutz</li><li>Cookie-Richtlinie</li><li>Datenschutzerklärung nach DSGVO</li></ul>
</footer>

<div class="abs bottombar">
  <p>© 2020 Psychotherapeutische Praxis - DIPL.-PSYCH. MIRIAM HOLLMANN. Alle Rechte vorbehalten.</p>
  <div class="up"><svg width="7" height="4" viewBox="0 0 14 8"><path d="M1 7l6-5 6 5" fill="none" stroke="#fff" stroke-width="2"/></svg></div>
</div>

</body>
</html>
```